Digitales Briefpapier für IT-Systemhaus
Zielgruppe
IT-Systemhaus mit dem Schwerpunkt Digitalisierung von Geschäftsprozessen. Ggf. Schlagwörter wie DMS, ECM, Digitalisierung Ihrer Prozesse unterbringen.
Aufgabenstellung
Digitale Vorlage (Word) um daraus dann ein PDF zu generieren. Anschrift usw. auf QXN.de

```html
<!DOCTYPE html>
<html lang="de">
<head>
<meta charset="utf-8">
<title>QXN.de Briefpapier</title>
<link rel="stylesheet" href="https://fonts.googleapis.com/css2?family=Open+Sans:wght@300;400;600;700&display=swap">
<style>
  :root {
    --brand-blue: #3263a8;
    --stripe: #bcc6e3;
    --ink: #3a3a3a;
    --paper: #ffffff;
    --mark: #555555;
  }
  * { margin: 0; padding: 0; box-sizing: border-box; }
  html, body { width: 847px; height: 1200px; overflow: hidden; background: var(--paper); }
  body { font-family: "Open Sans", Arial, sans-serif; color: var(--ink); }
  .letterhead { position: relative; width: 847px; height: 1200px; background: var(--paper); }
  .band { position: absolute; left: 0; width: 847px; }
  .band--top { top: 0; height: 88px; }
  .band--bottom { top: 1166px; height: 34px; }
  .brand-name {
    position: absolute; left: 78px; top: 18px;
    font-weight: 300; font-size: 44px; letter-spacing: 4px; color: var(--paper);
  }
  .tagline {
    position: absolute; right: 50px; top: 29px;
    font-size: 14.5px; color: var(--paper);
  }
  .address-window { position: absolute; left: 78px; top: 159px; width: 351px; height: 170px; }
  .sender-line {
    position: absolute; left: 45px; top: 20px;
    font-size: 7px; white-space: nowrap; border-bottom: 0.8px solid var(--ink); padding-bottom: 2px;
  }
  .sender-line .company { color: var(--brand-blue); }
  .sender-line .sep { display: inline-block; width: 0.7px; height: 8px; background: #999; margin: 0 4px; vertical-align: -1px; }
  .contact { position: absolute; left: 611px; top: 157px; font-size: 9.6px; line-height: 15px; }
  .contact__row { position: relative; padding-left: 22px; }
  .contact__row svg { position: absolute; left: 0; fill: var(--brand-blue); }
  .contact__company { color: var(--brand-blue); font-weight: 700; }
  .contact__row--phone { margin-top: 7px; }
  .contact__row--fax, .contact__row--mail { margin-top: 4px; }
  .contact__row--bank { margin-top: 11px; }
  .fold-mark { position: absolute; left: 29px; width: 6px; height: 8px; }
  .website {
    position: absolute; right: 46px; top: 1175px;
    font-weight: 700; font-size: 12.5px; color: var(--paper); letter-spacing: 0.3px;
    display: flex; align-items: center; gap: 6px;
  }
</style>
</head>
<body>
<main class="letterhead">
  <svg class="band band--top" viewBox="0 0 847 88" aria-hidden="true">
    <polygon points="0,0 847,0 847,57 381,57 364,88 0,88" fill="var(--brand-blue)"/>
    <polygon points="377,66 847,66 847,73 373,73" fill="var(--stripe)"/>
    <polygon points="370,80 847,80 847,88 366,88" fill="var(--stripe)"/>
  </svg>
  <div class="brand-name">QXN.de</div>
  <div class="tagline">DMS, ECM, Digitalisierung Ihrer Prozesse unterbringen.</div>

  <div class="address-window">
    <svg width="351" height="170" viewBox="0 0 351 170" aria-hidden="true" fill="none" stroke="var(--mark)" stroke-width="0.8">
      <path d="M0,30 V12 A12,12 0 0 1 12,0 H28"/>
      <path d="M323,0 H339 A12,12 0 0 1 351,12 V30"/>
      <path d="M0,140 V158 A12,12 0 0 0 12,170 H28"/>
      <path d="M323,170 H339 A12,12 0 0 0 351,158 V140"/>
    </svg>
    <div class="sender-line"><span class="company">QXN.de Systemhaus GmbH &amp; Co. KG</span><span class="sep"></span>Lindenweg 24b<span class="sep"></span>31275 Lehrte</div>
  </div>

  <section class="contact">
    <div class="contact__row">
      <svg width="18" height="18" viewBox="0 0 18 18" style="top:9px"><polygon points="1,2 17,9 1,16 5,9"/></svg>
      <div class="contact__company">QXN.de Systemhaus GmbH &amp; Co. KG</div>
      <div>Lindenweg 24b</div>
      <div>31275 Lehrte</div>
    </div>
    <div class="contact__row contact__row--phone">
      <svg width="14" height="14" viewBox="0 0 14 14" style="top:1px"><path d="M3,1 L5.5,4 L4,5.5 C5,8 6,9 8.5,10 L10,8.5 L13,11 L11,13 C6,12.5 1.5,8 1,3 Z"/></svg>
      +49 (511) 4807120
    </div>
    <div class="contact__row contact__row--fax">
      <svg width="14" height="14" viewBox="0 0 14 14" style="top:1px"><path d="M3,1 H10 V5 H3 Z M1,5 H13 V13 H1 Z" fill="none" stroke="var(--brand-blue)" stroke-width="1.2"/><rect x="3" y="8" width="8" height="1.2"/><rect x="3" y="10.5" width="8" height="1.2"/></svg>
      +49 (511) 48071299
    </div>
    <div class="contact__row contact__row--mail">
      <svg width="14" height="14" viewBox="0 0 14 14" style="top:1px"><rect x="1" y="3" width="12" height="9" rx="1"/><path d="M1.5,4 L7,8 L12.5,4" fill="none" stroke="#fff" stroke-width="1.2"/></svg>
      info(at)qxn.de
    </div>
    <div class="contact__row contact__row--bank">
      <svg width="14" height="14" viewBox="0 0 14 14" style="top:17px"><polygon points="7,1 13,4 1,4"/><rect x="2" y="5" width="1.6" height="6"/><rect x="5" y="5" width="1.6" height="6"/><rect x="7.6" y="5" width="1.6" height="6"/><rect x="10.4" y="5" width="1.6" height="6"/><rect x="1" y="11.5" width="12" height="1.5"/></svg>
      <div>Amtsgericht Hildesheim</div>
      <div>IBAN DE12 2505 0000 0123 4567 89</div>
      <div>BIC NOLADE2HXXX</div>
      <div>Ust. ID: DE301245876</div>
    </div>
  </section>

  <svg class="fold-mark" style="top:446px" viewBox="0 0 6 8" aria-hidden="true"><polygon points="0,0 6,4 0,8" fill="var(--brand-blue)"/></svg>
  <svg class="fold-mark" style="top:759px" viewBox="0 0 6 8" aria-hidden="true"><polygon points="0,0 6,4 0,8" fill="var(--brand-blue)"/></svg>

  <svg class="band band--bottom" viewBox="0 0 847 34" aria-hidden="true">
    <polygon points="0,2 540,2 537,8 0,8" fill="var(--stripe)"/>
    <polygon points="0,12 535,12 532,18 0,18" fill="var(--stripe)"/>
    <polygon points="542,2 847,2 847,34 0,34 0,22 530,22" fill="var(--brand-blue)"/>
  </svg>
  <div class="website">
    <svg width="14" height="14" viewBox="0 0 14 14" fill="none" stroke="#fff" stroke-width="1"><circle cx="7" cy="7" r="6"/><ellipse cx="7" cy="7" rx="2.6" ry="6"/><path d="M1,7 H13 M2,4 H12 M2,10 H12"/></svg>
    www.qxn.de
  </div>
</main>
</body>
</html>
```